Stretch on the Green with Mira

I want to advertise my Stretch on the Green classes for Summer. Classes are outside at the lovely local park. Holloway field. 83 Marangi St. Sandringham.
Classes are for beginners to advance levels.
Classes start Monday, October 17th.
Monday 6pm Beginners
Tuesday 6pm Intermediate
Thursday 6pm Intermediate/Advance
Saturday 9am All fitness levels
My Pilates classes are specially designed to help improve strength and flexibility but as well will also improve posture, reduce stress and develop control and endurance in the entire body.
Booking essential. Limited numbers so I can make sure the correct technique is always being followed.
For more info or to book contact details:
Mira 027358164
mira@corewithmira.net
www.corewithmira.net
$15 Per Session

Target Market(s)

Males and Females ages 35plus.

Industry/Entity Type

Fitness

Font styles to use
Sans Serif

Requirements
Must have
• My logo. Contact details. A Park that looks lovely to exercise at.
Nice to have
• Summer looking. Trees - inspiration to be exercising outside

```html
<!DOCTYPE html>
<html lang="en">
<head>
<meta charset="utf-8">
<title>Stretch on the Green with Mira</title>
<link rel="stylesheet" href="https://fonts.googleapis.com/css2?family=Oswald:wght@500;600&family=Open+Sans:wght@500&family=Arimo:ital,wght@0,400;0,700;1,700&display=swap">
<style>
  :root {
    --pink: #e883b6;
    --charcoal: #4d4d4d;
    --slate: #8e8e8e;
    --green: #006a55;
    --white: #ffffff;
    --grass: #8fae3e;
    --sea: #7fb3c9;
  }
  * { margin: 0; padding: 0; box-sizing: border-box; }
  html, body { width: 960px; height: 1200px; overflow: hidden; background: var(--charcoal); }
  .flyer { position: relative; width: 960px; height: 1200px; overflow: hidden; background: var(--charcoal); color: var(--white); font-family: "Arimo", Arial, sans-serif; }

  .hero {
    position: absolute; left: 0; top: 0; width: 960px; height: 520px;
    background: linear-gradient(180deg, #9cc3d2 0%, var(--sea) 14%, #c9c7b9 24%, #a9bb63 32%, var(--grass) 55%, #6f9231 100%);
  }

  .backdrop { position: absolute; left: 0; top: 0; width: 960px; height: 1200px; }

  .services { position: absolute; left: 56px; top: 418px; display: flex; gap: 15px; }
  .service { width: 160px; height: 160px; background: var(--green); padding: 3px 3px 0; }
  .service-photo { height: 120px; }
  .service-label {
    height: 37px; display: flex; align-items: center; justify-content: center; text-align: center;
    font-family: "Oswald", sans-serif; font-weight: 500; font-size: 14px; line-height: 1.15; letter-spacing: .2px; text-transform: uppercase;
  }
  .photo-studio { background: linear-gradient(160deg, #d9d5cf, #6f6a66); }
  .photo-duo { background: linear-gradient(160deg, #f1eeea, #b8a9a0); }
  .photo-group { background: linear-gradient(160deg, #e6e3e0, #8a8888); }
  .photo-postnatal { background: linear-gradient(160deg, #d8dbe0, #9aa7b8); }
  .photo-baby { background: linear-gradient(160deg, #fbfbfb, #e7e1da); }

  .headline { position: absolute; left: 53px; top: 600px; width: 420px; }
  .headline h1 {
    font-family: "Oswald", sans-serif; font-weight: 600; color: var(--pink);
    font-size: 44px; line-height: 45px; text-transform: uppercase; letter-spacing: -.3px;
    padding-bottom: 5px; border-bottom: 2px solid var(--white);
  }
  .location { position: absolute; left: 52px; top: 705px; font-family: "Open Sans", sans-serif; font-weight: 500; font-size: 20px; line-height: 24px; white-space: nowrap; }
  .intro { position: absolute; left: 53px; top: 762px; width: 418px; font-size: 17px; line-height: 22px; text-align: justify; color: #f2f2f2; }

  .contact { position: absolute; left: 53px; top: 884px; width: 440px; }
  .contact-heading { color: var(--pink); font-weight: 700; font-size: 30px; line-height: 28px; text-transform: uppercase; }
  .contact-phone { font-weight: 700; font-size: 52px; line-height: 56px; margin-top: 2px; }
  .contact-email { font-weight: 700; font-size: 33px; line-height: 36px; }

  .price {
    position: absolute; left: 53px; top: 1042px; width: 420px; height: 56px;
    background: var(--pink); border-radius: 0 28px 28px 0;
    display: flex; align-items: center; justify-content: center;
    font-weight: 700; font-size: 40px; letter-spacing: .5px; text-transform: uppercase;
  }

  .brand { position: absolute; left: 513px; top: 604px; width: 413px; text-align: center; }
  .brand-dot { width: 64px; height: 64px; border-radius: 50%; background: #767676; margin: 0 auto 18px; }
  .brand-name { font-family: "Oswald", sans-serif; font-weight: 500; color: var(--pink); font-size: 40px; line-height: 48px; letter-spacing: 3px; text-transform: uppercase; white-space: nowrap; }

  .schedule { position: absolute; left: 523px; top: 747px; width: 393px; }
  .levels {
    background: var(--green); height: 63px; border-radius: 4px 4px 0 0;
    display: flex; align-items: center; justify-content: center; text-align: center;
    font-family: "Oswald", sans-serif; font-weight: 500; font-size: 24px; line-height: 26px; text-transform: uppercase; letter-spacing: .3px;
  }
  .sessions { background: var(--slate); border-radius: 0 0 6px 6px; padding: 12px 16px 14px 16px; height: 316px; }
  .start-date { font-family: "Oswald", sans-serif; font-weight: 600; font-size: 21px; line-height: 28px; text-transform: uppercase; letter-spacing: -.4px; margin-bottom: 8px; white-space: nowrap; }
  .session { list-style: none; position: relative; padding-left: 26px; margin-bottom: 7px; }
  .session::before { content: ""; position: absolute; left: 4px; top: 10px; width: 9px; height: 9px; border-radius: 50%; background: var(--white); }
  .session-day { display: block; font-weight: 700; font-size: 24px; line-height: 27px; }
  .session-level { display: block; font-size: 24px; line-height: 27px; }

  .website { position: absolute; right: 42px; top: 1140px; font-weight: 700; font-style: italic; font-size: 38px; }
</style>
</head>
<body>
<main class="flyer">
  <div class="hero" role="img" aria-label="Photo of a woman stretching on the grass in a sunny seaside park with trees"></div>

  <svg class="backdrop" viewBox="0 0 960 1200" aria-hidden="true">
    <path d="M0 482 Q 470 600 960 468 L960 1200 L0 1200 Z" fill="var(--pink)"/>
    <path d="M0 500 Q 470 620 960 482 L960 1200 L0 1200 Z" fill="var(--charcoal)"/>
    <path d="M0 1108 Q 300 1172 960 1080 L960 1200 L0 1200 Z" fill="#d9d9d9"/>
    <path d="M0 1128 Q 300 1188 960 1096 L960 1200 L0 1200 Z" fill="var(--green)"/>
  </svg>

  <section class="services">
    <div class="service"><div class="service-photo photo-studio" role="img" aria-label="Photo of a woman doing a bridge on a mat"></div><p class="service-label">Group Pilates<br>Classes</p></div>
    <div class="service"><div class="service-photo photo-duo" role="img" aria-label="Photo of two people stretching with arms raised"></div><p class="service-label">Mobile Private<br>Pilates Sessions</p></div>
    <div class="service"><div class="service-photo photo-group" role="img" aria-label="Photo of a group class stretching together"></div><p class="service-label">Group Mobile<br>Pilates Sessions</p></div>
    <div class="service"><div class="service-photo photo-postnatal" role="img" aria-label="Photo of mothers exercising on mats with babies"></div><p class="service-label">Postnatal Mobile<br>Pilates Classes</p></div>
    <div class="service"><div class="service-photo photo-baby" role="img" aria-label="Photo of a mother lifting her baby while lying down"></div><p class="service-label">Mums and Bubs<br>Class</p></div>
  </section>

  <header class="headline"><h1>Stretch on the Green<br>Classes for Summer</h1></header>
  <p class="location">Classes are outside at the lovely local park.<br>Holloway field. 83 Marangi St. Sandringham.</p>
  <p class="intro">My Pilates classes are specially designed to help improve strength and flexibility but as well will also improve posture, reduce stress and develop control &amp; endurance in the entire body.</p>

  <section class="contact">
    <p class="contact-heading">For more info or to<br>book contact details:</p>
    <p class="contact-phone">Mira 027358164</p>
    <p class="contact-email">mira@corewithmira.net</p>
  </section>
  <p class="price">$15 per session</p>

  <div class="brand">
    <div class="brand-dot"></div>
    <p class="brand-name">Core with Mira</p>
  </div>

  <section class="schedule">
    <p class="levels">Classes are for beginners<br>to advance levels.</p>
    <div class="sessions">
      <p class="start-date">Classes start Monday, October 17th.</p>
      <ul>
        <li class="session"><span class="session-day">Monday 6pm</span><span class="session-level">Beginners</span></li>
        <li class="session"><span class="session-day">Tuesday 6pm</span><span class="session-level">Intermediate</span></li>
        <li class="session"><span class="session-day">Thursday 6pm</span><span class="session-level">Intermediate/Advance</span></li>
        <li class="session"><span class="session-day">Saturday 9am</span><span class="session-level">All fitness levels</span></li>
      </ul>
    </div>
  </section>

  <p class="website">www.corewithmira.net</p>
</main>
</body>
</html>
```